Plant based protein powders and bars in different flavors need a packaging design

I need a packaging design for a new company called "Vell Pastura". We develop plant based protein powders and Bars which are made with completely organic food ingredients and are completely free of preservative and artificial additives. The aim is to create something that speaks purity, Doesn't mislead the customer and signifies Pure and natural food. Sun gives life to vegetation and that's what we use to survive. We will use both stand-up pouches and tubs to sell our powder. So I need a packaging design for both.The protein bars are something where I would like to try and be creative with the packaging. There are multiple flavors. For each flavor we need a different color theme but the overall theme should remain the same.

Target Market(s)

working individuals who are looking for too busy to eat a complete nutritious meal or lack time to make one. Target consumer needs something that they can consume anytime they want, irrespective of the place they're at. Nutrition deprived people are our target consumers.

Industry/Entity Type

Nutrition

Font styles to use
Serif
Decorative

Colors

Designer to choose colors to be used in the design.

Requirements
Must have
• Unique Eye catching packaging design. Simple yet elegant. Something that says Pure and Simple yet powerful and effective.
Should not have
• Complex packaging that makes it harder for consumers to make a buying decision.

```html
<!DOCTYPE html>
<html lang="en">
<head>
<meta charset="utf-8">
<title>Vell Pastura — Plant Based Protein, Mint Chocolate</title>
<link rel="stylesheet" href="https://fonts.googleapis.com/css2?family=Cinzel:wght@700&family=Montserrat:wght@700&family=Open+Sans:wght@400;700&display=swap">
<style>
  :root {
    --backdrop: #e4e4e4;
    --label-light: #f7f7f7;
    --label-mid: #e3e5e6;
    --ink-grey: #4a4a4a;
    --orange-deep: #b8501c;
    --orange: #e0793a;
    --orange-light: #f2b46c;
    --mint: #5f9e22;
    --mint-circle: #2f9a3a;
    --chocolate: #5a2e18;
    --chocolate-dark: #3f1d0e;
    --white: #ffffff;
  }
  * { margin: 0; padding: 0; box-sizing: border-box; }
  html, body { width: 1200px; height: 918px; overflow: hidden; }
  body { background: var(--backdrop); position: relative; font-family: "Open Sans", sans-serif; }

  .pouch-front {
    position: absolute; left: 335px; top: 9px; width: 530px; height: 900px;
    background: linear-gradient(100deg, var(--label-mid) 0%, var(--label-light) 35%, var(--white) 55%, var(--label-mid) 100%);
    overflow: hidden;
  }
  .abs { position: absolute; }

  .brand {
    left: 0; width: 530px; top: 258px;
    display: flex; align-items: center; justify-content: center; gap: 12px;
  }
  .brand-dot { width: 16px; height: 16px; border-radius: 50%; background: var(--orange); }
  .brand-name {
    font-family: "Open Sans", sans-serif; font-weight: 400; font-size: 28px;
    color: var(--ink-grey);
  }

  .product-title {
    left: 0; width: 530px; top: 410px; text-align: center;
    font-family: "Cinzel", serif; font-weight: 700; font-size: 86px; line-height: 1;
    background: linear-gradient(90deg, var(--orange-deep) 0%, var(--orange) 40%, var(--orange-light) 100%);
    -webkit-background-clip: text; background-clip: text; color: transparent;
  }
  .product-subtitle {
    left: 0; width: 530px; top: 502px; text-align: center;
    font-family: "Montserrat", sans-serif; font-weight: 700; font-size: 14px;
    letter-spacing: 6px; color: var(--ink-grey);
  }

  .flavour-box {
    left: 86px; top: 589px; width: 369px; height: 52px;
    border: 1px solid var(--mint); border-right-color: var(--chocolate); border-bottom-color: var(--chocolate);
    display: flex; align-items: center; justify-content: center; gap: 10px;
    font-family: "Open Sans", sans-serif; font-weight: 700; font-size: 38px; letter-spacing: -0.5px;
  }
  .flavour-mint { color: var(--mint); }
  .flavour-chocolate { color: var(--chocolate); }

  .claims { right: 268px; top: 658px; text-align: right; list-style: none; }
  .claim { font-size: 9px; line-height: 22px; color: #333; }
  .claim::after {
    content: ""; display: inline-block; width: 5px; height: 5px; border-radius: 50%;
    background: var(--mint-circle); margin-left: 6px; vertical-align: middle;
  }
  .divider { left: 274px; top: 652px; width: 1px; height: 110px; background: #9a9a9a; }

  .stat {
    width: 26px; height: 26px; border-radius: 50%; background: var(--mint-circle);
    border: 1.5px solid #d6efd4; color: var(--white); text-align: center;
    font-weight: 700; font-size: 8px; line-height: 1; padding-top: 5px; left: 286px;
  }
  .stat small { display: block; font-size: 5px; font-weight: 400; margin-top: 1px; }

  .product-photo {
    left: 327px; top: 692px; width: 168px; height: 87px; border-radius: 6px;
    background: linear-gradient(160deg, #8a5232 0%, #6b3a20 55%, #9cc79a 100%);
    transform: skewY(-6deg);
  }
  .seal { left: 249px; top: 750px; width: 50px; height: 50px; border-radius: 50%; border: 2px solid var(--orange); }

  .hex-band {
    left: 0; top: 800px; width: 530px; height: 70px;
    background: linear-gradient(180deg, rgba(242,180,108,0) 0%, rgba(242,160,90,0.35) 60%, rgba(224,121,58,0.55) 100%);
  }
  .base-svg { left: 0; top: 800px; }
  .supplement-label {
    left: 224px; top: 838px; width: 100px; text-align: center;
    font-size: 11px; line-height: 20px; letter-spacing: 0.5px; color: #f3e6dc;
  }
</style>
</head>
<body>
  <main class="pouch-front">
    <div class="abs brand">
      <span class="brand-dot"></span>
      <span class="brand-name">Vell Pastura</span>
    </div>

    <h1 class="abs product-title">PROTEIN</h1>
    <p class="abs product-subtitle">COMPLETE PLANT BASED</p>

    <div class="abs flavour-box">
      <span class="flavour-mint">MINT</span><span class="flavour-chocolate">CHOCOLATE</span>
    </div>

    <ul class="abs claims">
      <li class="claim">100% VEGAN</li>
      <li class="claim">ALL NATURAL</li>
      <li class="claim">SOY FREE</li>
    </ul>
    <div class="abs divider"></div>

    <div class="abs stat" style="top:651px">20G<small>Protine</small></div>
    <div class="abs stat" style="top:680px">0G<small>Sugar</small></div>
    <div class="abs stat" style="top:710px">3G<small>Carbs</small></div>

    <div class="abs product-photo" role="img" aria-label="Photo of a broken mint chocolate bar with a fresh mint leaf"></div>

    <div class="abs seal" role="img" aria-label="Certification seal"></div>

    <div class="abs hex-band" role="img" aria-label="Orange honeycomb pattern"></div>

    <svg class="abs base-svg" width="530" height="100" viewBox="0 0 530 100" aria-hidden="true">
      <path d="M0 50 Q265 68 530 50 L530 100 L0 100 Z" fill="var(--chocolate)"/>
      <path d="M0 80 Q265 98 530 80 L530 100 L0 100 Z" fill="var(--chocolate-dark)"/>
      <polygon points="224,38 274,12 324,38 324,100 224,100" fill="var(--chocolate)"/>
      <polyline points="140,18 274,-28 408,18" fill="none" stroke="#9a9a9a" stroke-width="1"/>
    </svg>
    <p class="abs supplement-label">NUTRITION<br>SUPPLEMENT</p>
  </main>
</body>
</html>
```